Homebased childcare service

I own a homebased childcare service; we promote rural experiences. See website. We have a slogan 'Educational Excellence in a Nutshell' and a bunch of nuts as a logo but this needs to be stylised I think. Colours are orange, green and white/off white, I also want some rack cards, posters and possibly a booklet. I have also wondered about some greenery in the background such as a fern, for perhaps the rack card?

Industry/Entity Type

Childcare

Contact Information for Business Card

Kowhai Meadow Homebased Childcare
17 Pellow Lane, R D 4, Kerikeri, 0283
kowhaimeadow@examplemail.co.nz
www.kowhaimeadow.co.nz
09 738 2249 or 105 3927 064
Maree Dunstow, Service Provider, Dip Tchng ECE, B of Ed.

On the back I would like:

Introductory Offer
Fourth day Special

Other Services available:
Nannying
Out of School Care
Holiday Programme
Professional Development

```html
<!DOCTYPE html>
<html lang="en">
<head>
<meta charset="utf-8">
<title>Kowhai Meadow Homebased Childcare – Business Card</title>
<link href="https://fonts.googleapis.com/css2?family=Arimo:wght@400;700&family=Comfortaa:wght@400;600&display=swap" rel="stylesheet">
<style>
  :root {
    --bg: #e9e6e0;
    --card-white: #ffffff;
    --green: #7cc242;
    --green-dark: #5ea52a;
    --green-light: #b6e07f;
    --orange: #ef6b2a;
    --ink: #1d1d1d;
    --back-text: #2a2a3a;
  }
  * { margin: 0; padding: 0; box-sizing: border-box; }
  html, body { width: 1200px; height: 892px; overflow: hidden; background: var(--bg); }
  .canvas { position: relative; width: 1200px; height: 892px; }
  .card {
    position: absolute; left: 250px; width: 700px; height: 400px;
    background: var(--card-white); overflow: hidden;
    box-shadow: 0 4px 14px rgba(0,0,0,.18);
  }
  .card--front { top: 40px; }
  .card--back { top: 492px; }

  .front-art { position: absolute; inset: 0; }
  .holder { position: absolute; left: 40px; top: 36px; font-family: Arimo, sans-serif; color: var(--ink); }
  .holder__name { font-size: 36px; font-weight: 700; letter-spacing: -0.5px; }
  .holder__role, .holder__quals { font-size: 21px; line-height: 1.2; }
  .brand { position: absolute; right: 36px; top: 40px; display: flex; align-items: center; gap: 14px; }
  .brand__mark { width: 34px; height: 34px; border-radius: 50%; background: var(--green-dark); }
  .brand__name { font-family: Arimo, sans-serif; font-weight: 700; font-size: 30px; line-height: 1.05; color: var(--orange); }
  .contact { position: absolute; left: 318px; top: 262px; list-style: none; font-family: Arimo, sans-serif; font-size: 18px; color: var(--ink); }
  .contact__item { display: flex; align-items: center; gap: 10px; height: 26px; }
  .contact__icon { width: 20px; height: 20px; background: var(--orange); display: flex; align-items: center; justify-content: center; }
  .contact__icon svg { width: 13px; height: 13px; }
  .divider { position: absolute; left: 296px; top: 250px; width: 2px; height: 112px; background: var(--ink); }

  .back-photo {
    position: absolute; inset: 0;
    background: linear-gradient(180deg, #c9d3bd 0%, #b7c4a6 40%, #cfc6c8 70%, #d8d4d2 100%);
  }
  .back-veil { position: absolute; inset: 0; background: rgba(255,255,255,.35); }
  .services { position: absolute; left: 60px; top: 38px; font-family: Comfortaa, sans-serif; color: var(--back-text); }
  .services__heading { font-size: 27px; font-weight: 600; margin-bottom: 4px; }
  .services__list { list-style: none; margin: 0 0 22px 34px; }
  .services__list li { position: relative; padding-left: 28px; line-height: 1.4; }
  .services__list li::before {
    content: ""; position: absolute; left: 0; top: 50%; width: 9px; height: 9px;
    border: 2px solid var(--back-text); border-radius: 50%; transform: translateY(-50%);
  }
  .services__list--main li { font-size: 21px; }
  .services__list--other li { font-size: 27px; }
</style>
</head>
<body>
<div class="canvas">

  <section class="card card--front" aria-label="Business card front">
    <svg class="front-art" viewBox="0 0 700 400" width="700" height="400" aria-hidden="true">
      <defs>
        <linearGradient id="greenFill" x1="0" y1="0" x2="1" y2="1">
          <stop offset="0" stop-color="#6db536"/>
          <stop offset="0.6" stop-color="#82c646"/>
          <stop offset="1" stop-color="#9bd35a"/>
        </linearGradient>
        <path id="sloganCurve" d="M330,190 C440,230 540,300 690,372"/>
      </defs>
      <path d="M0,0 L40,0 C200,30 330,120 450,215 C540,290 620,360 700,378 L700,400 L0,400 Z" fill="url(#greenFill)"/>
      <path d="M40,0 C200,30 330,120 450,215 C540,290 620,360 700,378" fill="none" stroke="#b6e07f" stroke-width="10" opacity=".7"/>
      <path d="M0,30 C190,50 320,140 440,235 C530,305 610,370 700,392" fill="none" stroke="#ffffff" stroke-width="3" opacity=".45"/>
      <text font-family="Arimo, sans-serif" font-size="19" fill="#ef6b2a">
        <textPath href="#sloganCurve" startOffset="8%">educational excellence in a nutshell</textPath>
      </text>
    </svg>

    <div class="holder">
      <p class="holder__name">Maree Dunstow</p>
      <p class="holder__role">Service Provider</p>
      <p class="holder__quals">Dip Tchng ECE, B of Ed</p>
    </div>

    <div class="brand">
      <span class="brand__mark"></span>
      <p class="brand__name">Kowhai Meadow<br>Homebased Childcare</p>
    </div>

    <div class="divider"></div>
    <ul class="contact">
      <li class="contact__item"><span class="contact__icon"><svg viewBox="0 0 24 24"><path fill="#fff" d="M6.6 10.8a15 15 0 0 0 6.6 6.6l2.2-2.2c.3-.3.7-.4 1-.2 1.1.4 2.3.6 3.6.6.6 0 1 .4 1 1V20c0 .6-.4 1-1 1A17 17 0 0 1 3 4c0-.6.4-1 1-1h3.5c.6 0 1 .4 1 1 0 1.3.2 2.5.6 3.6.1.3 0 .7-.2 1z"/></svg></span>09 738 2249</li>
      <li class="contact__item"><span class="contact__icon"><svg viewBox="0 0 24 24"><rect x="7" y="2" width="10" height="20" rx="2" fill="#fff"/></svg></span>105 3927 064</li>
      <li class="contact__item"><span class="contact__icon"><svg viewBox="0 0 24 24"><circle cx="12" cy="12" r="9" fill="none" stroke="#fff" stroke-width="2.5"/></svg></span>www.kowhaimeadow.co.nz</li>
      <li class="contact__item"><span class="contact__icon"><svg viewBox="0 0 24 24"><rect x="2" y="5" width="20" height="14" fill="#fff"/><path d="M2 5l10 8 10-8" fill="none" stroke="#ef6b2a" stroke-width="2"/></svg></span>kowhaimeadow@examplemail.co.nz</li>
    </ul>
  </section>

  <section class="card card--back" aria-label="Business card back">
    <div class="back-photo" role="img" aria-label="Photo of young children in raincoats and gumboots walking through puddles on a rural road, one holding an umbrella"></div>
    <div class="back-veil"></div>
    <div class="services">
      <h2 class="services__heading">Main services available:</h2>
      <ul class="services__list services__list--main">
        <li>Introductory Offer</li>
        <li>Fourth day Special</li>
      </ul>
      <h2 class="services__heading">Other Services available:</h2>
      <ul class="services__list services__list--other">
        <li>Nannying</li>
        <li>Out of School Care</li>
        <li>Holiday Programme</li>
        <li>Professional Development</li>
      </ul>
    </div>
  </section>

</div>
</body>
</html>
```